Promotional Ad/Flyer - Kavo Leasing

A division of our company, Kavo Leasing (kavo-leasing.example) is celebrating its 1-year anniversary in September and we would like to run a promotion. I am looking to have a promotional ad/flyer made-up for email mailings and LinkedIn posts and possibly have on our site. Have plenty of product photos to share if needed, not a prerequisite to use our product in the ad but open to it. Can also be cool graphics as well. We want to capture the viewers attention with the 30 DAYS FREE! The message is simple:
We are celebrating our 1-Year Anniversary by offering a Special Peak-Season Promotion!

FREE RENTALS for 30 days with a minimum 30-Day rental!

Valid from Sep. 1 - Dec. 31 & while supplies last.

Please contact our sales department for more details.

Email: quotes@kavo-leasing.example
Phone: +1-555-284-9317

```html
<!DOCTYPE html>
<html lang="en">
<head>
<meta charset="utf-8">
<title>Kavo Leasing – 1-Year Anniversary Promotion</title>
<link rel="stylesheet" href="https://fonts.googleapis.com/css2?family=Anton&family=Montserrat:wght@300;400;500;600&family=Roboto+Condensed:wght@400;700&display=swap">
<style>
  :root {
    --brand-blue: #4f72bf;
    --brand-blue-light: #5a7cc6;
    --brand-blue-deep: #466ab6;
    --pill-text: #4c70be;
    --white: #ffffff;
  }
  * { margin: 0; padding: 0; box-sizing: border-box; }
  html, body { width: 873px; height: 1200px; overflow: hidden; background: var(--brand-blue); }
  .flyer {
    position: relative;
    width: 873px;
    height: 1200px;
    overflow: hidden;
    color: var(--white);
    font-family: "Montserrat", sans-serif;
  }
  .flyer__backdrop {
    position: absolute; inset: 0;
    background:
      linear-gradient(160deg, transparent 55%, rgba(255,255,255,0.06) 56%, rgba(255,255,255,0.03) 75%, transparent 76%),
      linear-gradient(90deg, var(--brand-blue-light) 0%, var(--brand-blue-deep) 35%, var(--brand-blue) 65%, var(--brand-blue-light) 100%);
  }
  .line {
    position: absolute; left: 0; right: 0;
    text-align: center; white-space: nowrap; line-height: 1;
    transform: translateY(-50%);
  }
  .brand {
    position: absolute; left: 0; right: 0; top: 160px;
    display: flex; justify-content: center; align-items: center; gap: 14px;
    transform: translateY(-50%);
  }
  .brand__mark { width: 30px; height: 30px; background: var(--white); }
  .brand__name { font-size: 40px; font-weight: 500; letter-spacing: 1px; }
  .site-credit { top: 377px; font-size: 12px; font-weight: 500; letter-spacing: 1.6px; }
  .site-credit__sep { margin: 0 10px; }
  .kicker {
    position: absolute; top: 451px; left: 116px; right: 118px;
    display: flex; align-items: center; gap: 10px;
    transform: translateY(-50%);
  }
  .kicker__rule { flex: 1; height: 2px; background: var(--white); }
  .kicker__text { font-size: 22px; font-weight: 600; letter-spacing: 0.3px; white-space: nowrap; }
  .anniversary { top: 505px; font-size: 50px; font-weight: 500; letter-spacing: 1px; }
  .offer-intro { top: 546px; font-size: 20.5px; font-weight: 300; }
  .headline-box {
    position: absolute; left: 111px; width: 653px; top: 574px; height: 135px;
    border: 2px solid var(--white);
    display: flex; align-items: center; justify-content: center;
  }
  .headline-box__text {
    font-family: "Anton", sans-serif; font-size: 104px; line-height: 1;
    letter-spacing: 1px; white-space: nowrap; transform: scaleY(1.12);
  }
  .duration { top: 766px; font-size: 90px; font-weight: 500; letter-spacing: 1px; }
  .minimum { top: 830px; font-size: 30px; font-weight: 600; letter-spacing: 0.2px; }
  .validity {
    position: absolute; left: 111px; width: 651px; top: 862px; height: 59px;
    background: var(--white); border-radius: 20px;
    display: flex; align-items: center; justify-content: center;
    color: var(--pill-text); font-size: 21px; font-weight: 300; white-space: nowrap;
  }
  .contact-call {
    top: 962px; font-family: "Roboto Condensed", sans-serif;
    font-size: 21px; font-weight: 700; transform: translateY(-50%) scaleY(1.05);
  }
  .contact-icon {
    position: absolute; left: 419px; width: 34px; height: 34px;
    transform: translateY(-50%);
  }
  .contact-icon--email { top: 1001px; }
  .contact-icon--phone { top: 1076px; }
  .contact-detail { font-family: "Roboto Condensed", sans-serif; font-size: 20px; font-weight: 400; }
  .contact-detail--email { top: 1039px; }
  .contact-detail--phone { top: 1113px; }
</style>
</head>
<body>
<main class="flyer">
  <div class="flyer__backdrop" role="img" aria-label="Faint photo of an air cargo container in brand blue, scattered with confetti, streamers and stars"></div>

  <div class="brand">
    <span class="brand__mark"></span>
    <span class="brand__name">Kavo Leasing</span>
  </div>

  <p class="line site-credit">KAVO-LEASING.EXAMPLE<span class="site-credit__sep">|</span>BY NORVANE</p>

  <div class="kicker">
    <span class="kicker__rule"></span>
    <span class="kicker__text">WE ARE CELEBRATING OUR</span>
    <span class="kicker__rule"></span>
  </div>

  <h1 class="line anniversary">1-YEAR ANNIVERSARY</h1>
  <p class="line offer-intro">BY OFFERING A SPECIAL PEAK-SEASON PROMOTION!</p>

  <div class="headline-box">
    <h2 class="headline-box__text">FREE RENTALS</h2>
  </div>

  <p class="line duration">FOR 30 DAYS</p>
  <p class="line minimum">WITH A MINIMUM 30-DAY RENTAL!</p>

  <p class="validity">VALID FROM SEP. 1 - DEC. 31 &amp; WHILE SUPPLIES LAST.</p>

  <p class="line contact-call">PLEASE CONTACT OUR SALES DEPARTMENT FOR MORE DETAILS</p>

  <svg class="contact-icon contact-icon--email" viewBox="0 0 34 34" aria-hidden="true">
    <circle cx="17" cy="17" r="17" fill="#ffffff"/>
    <rect x="8" y="11" width="18" height="12" rx="1.5" fill="none" stroke="#4f72bf" stroke-width="2"/>
    <path d="M8.5 11.8 L17 18.5 L25.5 11.8 M8.5 22.2 L14.5 16.8 M25.5 22.2 L19.5 16.8" fill="none" stroke="#4f72bf" stroke-width="1.8" stroke-linejoin="round"/>
  </svg>
  <p class="line contact-detail contact-detail--email">quotes@kavo-leasing.example</p>

  <svg class="contact-icon contact-icon--phone" viewBox="0 0 34 34" aria-hidden="true">
    <circle cx="17" cy="17" r="17" fill="#ffffff"/>
    <path d="M11.5 8.5 C10 9.5 9 11 9.5 13 C10.8 18 15.5 23 21 24.6 C23 25.2 24.6 24.2 25.6 22.6 L22.6 19.6 C22 19 21.2 19.1 20.6 19.6 L19.5 20.6 C17 19.4 14.8 17.2 13.6 14.6 L14.6 13.5 C15.1 12.9 15.2 12.1 14.6 11.5 Z" fill="#4f72bf"/>
  </svg>
  <p class="line contact-detail contact-detail--phone">+1-555-284-9317</p>
</main>
</body>
</html>
```